A website for a Maltese Law Firm

Our law firm needs a website to further its business. The site should have a simple yet effective design. We would need the following sections: About us, Practice Areas, About Malta, Contact. These should be further split as follows:

About us: Our firm, Our values, What others say, Offices

Practice Areas: Crimimal, Citizenship & Residence, Overseas Patron Scheme, Criminal Defence, Civil Litigation, Arbitration and ADR, Commercial and Corporate, Media Law.

About Malta: just one section.

Contact: Just one section

We would also need a news feed at the front of the site to include latest news regarding our cases.

At the bottom we need a section for our Terms and a Privacy Statement.

Our logo is being attached.

Target Market(s)

All clients looking for legal assistance in Malta

Industry/Entity Type

Legal

Coding

Coded - Design and coding required

Number of Pages Required

1 page

Requirements
Must have
• It must be simple yet striking.

```html
<!DOCTYPE html>
<html lang="en">
<head>
<meta charset="utf-8">
<title>Galea &amp; Zammit Advocates</title>
<link rel="stylesheet" href="https://fonts.googleapis.com/css2?family=Raleway:wght@400;500;600;700&family=Open+Sans:ital,wght@0,400;0,600;0,700;1,400&family=Roboto+Slab:wght@400&display=swap">
<style>
:root{
  --ink:#222222;
  --text:#333333;
  --muted:#555555;
  --topbar:#151515;
  --panel:#333333;
  --field:#6e6e6e;
  --soft-bg:#f6f6f6;
  --band:#9a9a9a;
  --footer:#232323;
  --footer-base:#111111;
  --rule:#bdbdbd;
  --white:#ffffff;
}
*{box-sizing:border-box;margin:0;padding:0}
html,body{width:1200px;height:2493px;overflow:hidden;background:var(--white)}
body{position:relative;font-family:"Open Sans",Arial,sans-serif;color:var(--text)}
.abs{position:absolute}
a{color:inherit;text-decoration:none}

/* top bar */
.topbar{left:0;top:0;width:1200px;height:37px;background:var(--topbar)}
.social{display:flex;gap:8px}
.social span{display:block;width:20px;height:20px;border:1.5px solid #cfcfcf}
.consult-tab{left:462px;top:0;width:279px;height:44px;background:var(--white);border:1px solid #999;border-top:none;font:500 15px "Raleway",sans-serif;color:var(--ink);display:flex;align-items:center;justify-content:center;box-shadow:0 2px 4px rgba(0,0,0,.3)}
.top-contact{top:8px;display:flex;align-items:center;gap:10px;color:#ddd;font-size:13px}
.top-contact svg{width:22px;height:22px}

/* header */
.header{left:0;top:37px;width:1200px;height:96px;background:var(--white)}
.brand{left:83px;top:72px;width:258px;font:500 21px/26px "Raleway",sans-serif;color:var(--ink);white-space:nowrap}
.nav{left:404px;top:88px;display:flex;align-items:center;font:400 14px "Raleway",sans-serif;color:#777}
.nav a{padding:0 13px;border-left:1px solid #ccc;line-height:18px}
.nav a:first-child{border-left:none;padding-left:0;color:var(--ink)}

/* hero */
.hero{left:0;top:133px;width:1200px;height:507px;background:linear-gradient(90deg,#3a2410 0%,#7a5530 22%,#3c3026 45%,#2d3038 65%,#c9c2b8 88%,#efeae3 100%)}
.hero-caption{left:95px;top:329px;width:656px;height:115px;background:rgba(35,35,35,.72);padding:22px 30px;font:500 28px/42px "Raleway",sans-serif;color:var(--white)}
.hero-arrow{width:28px;height:28px;border-radius:50%;background:var(--white);top:372px}

/* about */
.section-title{font:400 27px "Raleway",sans-serif;color:var(--ink)}
.about-title{left:83px;top:700px;width:697px;padding-bottom:8px;border-bottom:1px solid var(--rule)}
.about-copy{left:83px;top:754px;width:697px;font-size:12px;line-height:20px;color:var(--text)}
.btn-dark{background:#111;color:var(--white);font:700 13px "Open Sans",sans-serif;display:flex;align-items:center;justify-content:center}
.read-more{left:83px;top:866px;width:103px;height:29px}
.feature{top:922px;width:221px;height:88px;border:1px solid #ccc;background:var(--white);padding:12px 10px;display:flex;gap:12px}
.feature svg{width:60px;height:60px;flex:none}
.feature h3{font:400 15px "Raleway",sans-serif;color:var(--ink);margin-bottom:4px}
.feature p{font-size:11.5px;line-height:17px;color:var(--text)}

.enquiry{left:811px;top:683px;width:306px;height:326px;background:var(--panel);box-shadow:0 2px 6px rgba(0,0,0,.35)}
.enquiry h2{position:absolute;left:18px;top:15px;font:400 20px/24px "Raleway",sans-serif;color:var(--white)}
.field{position:absolute;left:15px;width:278px;background:var(--field);color:#eee;font-size:12.5px;padding:8px 10px}
.submit{left:828px;top:969px;width:104px;height:30px;font-size:13px;letter-spacing:.5px}

/* practice areas */
.practice{left:0;top:1064px;width:1200px;height:724px;background:var(--soft-bg)}
.practice-title{left:0;top:1105px;width:1200px;text-align:center}
.practice-title span{display:inline-block;padding-bottom:6px;border-bottom:1px solid var(--rule)}
.tile{width:254px;height:221px}
.tile-label{width:254px;text-align:center;font:700 15px "Raleway",sans-serif;color:var(--ink)}

/* cta */
.cta{left:0;top:1788px;width:1200px;height:62px;background:var(--band);color:var(--white);font:400 30px "Roboto Slab",serif;display:flex;align-items:center;justify-content:center}

/* cases & testimonials */
.col-title{top:1900px;padding-bottom:10px;border-bottom:1px solid var(--rule);display:flex;justify-content:space-between;align-items:flex-end}
.col-title .arrows{font:400 18px "Open Sans",sans-serif;letter-spacing:4px;color:var(--ink)}
.case{left:85px;width:487px;display:flex;gap:13px}
.date{width:45px;flex:none;text-align:center}
.date .day{background:#8c8c8c;color:var(--white);font-size:14px;height:33px;line-height:33px}
.date .mon{background:#111;color:var(--white);font:700 11px "Open Sans",sans-serif;height:22px;line-height:22px}
.case h4{font:700 12.5px "Open Sans",sans-serif;color:var(--ink);margin-bottom:4px}
.case p{font-size:12px;line-height:20px;color:var(--text)}
.quote-box{left:602px;top:1961px;width:515px;height:148px;border:1px solid #ccc;padding:14px 22px 10px 46px;font:italic 12px/22px "Open Sans",sans-serif;color:var(--text)}
.quote-mark{font:700 40px/1 Georgia,serif;color:#ccc}
.avatar{left:600px;top:2129px;width:52px;height:53px;background:linear-gradient(#d8d8d8,#a9a9a9)}
.client-name{left:665px;top:2150px;font:700 13px "Open Sans",sans-serif;color:var(--ink)}

/* footer */
.footer{left:0;top:2224px;width:1200px;height:241px;background:var(--footer)}
.footer-heading{font:400 15px "Raleway",sans-serif;color:var(--white)}
.links{left:90px;top:2290px;list-style:none;color:#ddd;font-size:12px;line-height:22.3px}
.links li::before{content:"›";color:#888;margin-right:12px}
.divider{top:2254px;width:1px;height:190px;background:#3a3a3a}
.contact-line{left:306px;display:flex;gap:10px;color:#ddd;font-size:12px;line-height:17px}
.contact-line svg{width:16px;height:16px;flex:none;margin-top:1px}
.map{left:587px;top:2254px;width:262px;height:169px;background:linear-gradient(135deg,#dedbd2 0%,#e8e4da 45%,#a8c6e0 70%,#8fb4d8 100%);border:3px solid #555}
.foot-brand{left:896px;top:2306px;width:226px;text-align:center;font:500 16px "Raleway",sans-serif;color:#aaa;white-space:nowrap}
.follow{left:920px;top:2356px;display:flex;align-items:center;gap:8px;color:var(--white);font-size:12px}
.follow .social span{border-color:#ddd}
.copyright{left:0;top:2465px;width:1200px;height:28px;background:var(--footer-base);color:#ddd;font-size:11px;display:flex;align-items:center;justify-content:center}
</style>
</head>
<body>

<!-- top bar -->
<div class="abs topbar"></div>
<div class="abs social" style="left:83px;top:8px"><span></span><span></span><span></span><span></span></div>
<div class="abs consult-tab">Schedule Free Consultation</div>
<div class="abs top-contact" style="left:786px">
  <svg viewBox="0 0 22 22"><rect x=".5" y=".5" width="21" height="21" fill="none" stroke="#ccc"/><path d="M7 5l2.5 3-1.4 1.6a8 8 0 0 0 4.3 4.3L14 12.5l3 2.5-1.5 2A10 10 0 0 1 5 6.5z" fill="#ccc"/></svg>
  <span>356 2000 4410</span>
</div>
<div class="abs top-contact" style="left:928px">
  <svg viewBox="0 0 22 22"><rect x=".5" y=".5" width="21" height="21" fill="none" stroke="#ccc"/><rect x="5" y="7" width="12" height="8" fill="#ccc"/><path d="M5 7l6 4 6-4" fill="none" stroke="#151515" stroke-width="1.2"/></svg>
  <span>office@gzadvocates.example</span>
</div>

<!-- header -->
<header class="abs header"></header>
<div class="abs brand">Galea &amp; Zammit Advocates</div>
<nav class="abs nav">
  <a href="#">HOME</a><a href="#">ABOUT US</a><a href="#">OUR FIRM</a><a href="#">OUR VALUES</a><a href="#">WHAT OTHERS SAY</a><a href="#">OFFICES</a><a href="#">CONTACT US</a>
</nav>

<!-- hero -->
<div class="abs hero" role="img" aria-label="Lawyer in a suit signing a document in front of law library shelves"></div>
<div class="abs hero-caption">Get Qualified Legal Advice In Malta<br>For Arbitration &amp; ADR</div>
<svg class="abs hero-arrow" style="left:54px" viewBox="0 0 28 28"><circle cx="14" cy="14" r="14" fill="#fff"/><path d="M16 9l-5 5 5 5" fill="none" stroke="#222" stroke-width="2"/></svg>
<svg class="abs hero-arrow" style="left:1116px" viewBox="0 0 28 28"><circle cx="14" cy="14" r="14" fill="#fff"/><path d="M12 9l5 5-5 5" fill="none" stroke="#222" stroke-width="2"/></svg>

<!-- about -->
<h2 class="abs section-title about-title">About Galea &amp; Zammit Advocates</h2>
<p class="abs about-copy">Lorem ipsum dolor sit amet, consectetuer adipiscing elit, sed diam nonummy nibh euismod tincidunt ut laoreet dolore magna aliquam erat volutpat. Ut wisi enim ad minim veniam, quis nostrud exerci tation ullamcorper suscipit lobortis nisl ut aliquip ex ea commodo consequat. Duis autem vel eum iriure dolor in hendrerit in vulputate velit esse molestie consequat, vel illum dolore eu feugiat nulla facilisis at vero eros et accumsan et iusto odio dignissim qui blandit praesent luptatum zzril delenit augue duis dolore te feugait nulla facilisi.</p>
<a class="abs btn-dark read-more" href="#">Read More</a>

<div class="abs feature" style="left:83px">
  <svg viewBox="0 0 60 60"><g fill="#444"><rect x="28" y="10" width="4" height="38"/><rect x="14" y="18" width="32" height="3"/><rect x="20" y="48" width="20" height="4"/><path d="M8 34l8-14 8 14z"/><path d="M36 34l8-14 8 14z"/></g></svg>
  <div><h3>Our Firm</h3><p>Lorem ipsum dolor sit consectetuer adipiscn</p></div>
</div>
<div class="abs feature" style="left:321px">
  <svg viewBox="0 0 60 60"><path d="M4 24l14-6 12 8 12-8 14 6v10L44 42l-14 4-14-8L4 34z" fill="#444"/></svg>
  <div><h3>Our Values</h3><p>Lorem ipsum dolor sit consectetuer adipiscn</p></div>
</div>
<div class="abs feature" style="left:560px">
  <svg viewBox="0 0 60 60"><g fill="#444"><rect x="6" y="28" width="12" height="22"/><rect x="22" y="20" width="16" height="30"/><rect x="42" y="28" width="12" height="22"/><path d="M22 20a8 8 0 0 1 16 0z"/></g></svg>
  <div><h3>About Malta</h3><p>Lorem ipsum dolor sit consectetuer adipiscn</p></div>
</div>

<form class="abs enquiry">
  <h2>Request for Free<br>Consulatation</h2>
  <div class="field" style="top:77px;height:35px">Name</div>
  <div class="field" style="top:121px;height:37px">Email</div>
  <div class="field" style="top:166px;height:37px">Inquiry Tpye</div>
  <div class="field" style="top:209px;height:64px">Message</div>
</form>
<a class="abs btn-dark submit" href="#">SUBMIT</a>

<!-- practice areas -->
<section class="abs practice"></section>
<h2 class="abs section-title practice-title"><span>Our Practice Areas</span></h2>

<div class="abs tile" style="left:83px;top:1187px;background:linear-gradient(135deg,#8a4a22,#c79a6a 55%,#e8dccb)" role="img" aria-label="Judge's gavel resting on a criminal law document"></div>
<div class="abs tile" style="left:344px;top:1187px;background:linear-gradient(160deg,#1f2a52,#3a4670 60%,#5a5e7a)" role="img" aria-label="Close-up of a passport cover"></div>
<div class="abs tile" style="left:603px;top:1187px;background:linear-gradient(150deg,#c7d6e6,#7b8da6 50%,#3c3f46)" role="img" aria-label="Businessman signing an investment agreement at a desk"></div>
<div class="abs tile" style="left:863px;top:1187px;background:linear-gradient(160deg,#e4eef6,#9fb6cc 55%,#4e6078)" role="img" aria-label="Business people meeting by a window with a contract on the table"></div>
<div class="abs tile-label" style="left:83px;top:1426px">Crimimal</div>
<div class="abs tile-label" style="left:344px;top:1426px">Citizenship &amp; Residence</div>
<div class="abs tile-label" style="left:603px;top:1426px">Overseas Patron Scheme</div>
<div class="abs tile-label" style="left:863px;top:1426px">Commercial &amp; Corporate</div>

<div class="abs tile" style="left:83px;top:1494px;background:linear-gradient(160deg,#3a3f4a,#6b6660 60%,#a09a90)" role="img" aria-label="Person in handcuffs being escorted"></div>
<div class="abs tile" style="left:344px;top:1494px;background:linear-gradient(160deg,#121212,#5a3a1e 60%,#b8863e)" role="img" aria-label="Scales of justice and law books for civil litigation"></div>
<div class="abs tile" style="left:603px;top:1494px;background:linear-gradient(150deg,#a9c2db,#4c5f78 50%,#1e2430)" role="img" aria-label="Business people standing around a conference table"></div>
<div class="abs tile" style="left:863px;top:1494px;background:linear-gradient(150deg,#7a3a10,#b0662a 50%,#e6e0d8)" role="img" aria-label="Wooden gavel beside a computer keyboard"></div>
<div class="abs tile-label" style="left:83px;top:1738px">Criminal Defence</div>
<div class="abs tile-label" style="left:344px;top:1738px">Civil Litigation</div>
<div class="abs tile-label" style="left:603px;top:1738px">Arbitration &amp; ADR</div>
<div class="abs tile-label" style="left:863px;top:1738px">Media Law</div>

<!-- call to action -->
<div class="abs cta">Call Us 356 2000 4410&nbsp; At&nbsp; Or Contact Us Online For A Free Estimate</div>

<!-- recent case studies -->
<div class="abs col-title" style="left:83px;width:489px"><h2 class="section-title">Recent Case Studies</h2><span class="arrows">‹›</span></div>
<article class="abs case" style="top:1961px">
  <div class="date"><div class="day">23</div><div class="mon">MAR</div></div>
  <div><h4>Lorem Ispum the dunny rect</h4><p>Lorem ipsum dolor sit amet, consectetuer adipiscing elit, sed diam nonummy nibh euismod tincidunt ut laoreet dolore magna</p></div>
</article>
<article class="abs case" style="top:2041px">
  <div class="date"><div class="day">23</div><div class="mon">MAR</div></div>
  <div><h4>Lorem Ispum the dunny rect</h4><p>Lorem ipsum dolor sit amet, consectetuer adipiscing elit, sed diam nonummy nibh euismod tincidunt ut laoreet dolore magna</p></div>
</article>
<article class="abs case" style="top:2121px">
  <div class="date"><div class="day">23</div><div class="mon">MAR</div></div>
  <div><h4>Lorem Ispum the dunny rect</h4><p>Lorem ipsum dolor sit amet, consectetuer adipiscing elit, sed diam nonummy nibh euismod tincidunt ut laoreet dolore magna</p></div>
</article>

<!-- testimonials -->
<div class="abs col-title" style="left:602px;width:515px"><h2 class="section-title">Client Testimonials</h2><span class="arrows">‹›</span></div>
<blockquote class="abs quote-box">
  <span class="abs quote-mark" style="left:14px;top:10px">“</span>
  Lorem ipsum dolor sit amet, consectetuer adipiscing elit, sed diam nonummy nibh euismod tincidunt ut laoreet dolore magna aliquam erat volutpat. Ut wisi enim ad minim veniam, quis nostrud exerci tation ullamcorper suscipit lobortis nisl ut aliquip ex ea commodo consequat. Duis autem vel eum iriure dolor in hendrerit in vulputate velit esse molestie consequat, vel illum dolore eu feugiat
  <span class="abs quote-mark" style="left:424px;top:112px">”</span>
</blockquote>
<div class="abs avatar" role="img" aria-label="Client portrait"></div>
<div class="abs client-name">Paul Grech</div>

<!-- footer -->
<footer class="abs footer"></footer>
<h4 class="abs footer-heading" style="left:90px;top:2250px">Quick Links</h4>
<ul class="abs links">
  <li>Home</li><li>About Us</li><li>Our Firm</li><li>Our Values</li><li>What Others Say</li><li>Offices</li><li>Contact Us</li>
</ul>
<div class="abs divider" style="left:275px"></div>
<h4 class="abs footer-heading" style="left:311px;top:2250px">Contact Details</h4>
<div class="abs contact-line" style="top:2290px">
  <svg viewBox="0 0 16 16"><rect x=".5" y=".5" width="15" height="15" fill="none" stroke="#ccc"/><path d="M8 3a3 3 0 0 1 3 3c0 2-3 6-3 6S5 8 5 6a3 3 0 0 1 3-3z" fill="#ccc"/></svg>
  <span>12/4, Harbour Lane, Valletta<br>88, Olive Grove Street, Birkirkara</span>
</div>
<div class="abs contact-line" style="top:2340px">
  <svg viewBox="0 0 16 16"><rect x=".5" y=".5" width="15" height="15" fill="none" stroke="#ccc"/><path d="M5 3.5l2 2.2-1 1.2a6 6 0 0 0 3.1 3.1l1.2-1 2.2 2-1 1.5A7.5 7.5 0 0 1 3.5 4.5z" fill="#ccc"/></svg>
  <span>356 2000 4410 ( Valletta )</span>
</div>
<div class="abs contact-line" style="top:2372px">
  <svg viewBox="0 0 16 16"><rect x=".5" y=".5" width="15" height="15" fill="none" stroke="#ccc"/><path d="M5 3.5l2 2.2-1 1.2a6 6 0 0 0 3.1 3.1l1.2-1 2.2 2-1 1.5A7.5 7.5 0 0 1 3.5 4.5z" fill="#ccc"/></svg>
  <span>356 2000 5520 (Birkirkara )</span>
</div>
<div class="abs contact-line" style="top:2402px">
  <svg viewBox="0 0 16 16"><rect x=".5" y=".5" width="15" height="15" fill="none" stroke="#ccc"/><rect x="3.5" y="5" width="9" height="6" fill="#ccc"/><path d="M3.5 5l4.5 3 4.5-3" fill="none" stroke="#232323"/></svg>
  <span>office@gzadvocates.example</span>
</div>
<div class="abs divider" style="left:546px"></div>
<div class="abs map" role="img" aria-label="Street map of Malta showing office locations"></div>
<div class="abs divider" style="left:880px"></div>
<div class="abs foot-brand">Galea &amp; Zammit Advocates</div>
<div class="abs follow"><span>Follow us</span><div class="social"><span></span><span></span><span></span><span></span></div></div>
<div class="abs copyright">Copyright © 2016 Galea &amp; Zammit Advocates. All rights reserved.</div>

</body>
</html>
```